New logo and wordpress design for Brightmoor-hub.org

We run a website that collates profiles/interviews of individuals who have completed a PhD and moved away from a traditional academix career path into something related. This is often related to the field they studied in, such as publishing, government policy, consulting, teaching and many other things. The website https://brightmoor-hub.org aims to give students and researchers ideas about what paths they can take their career on.

We would like to refresh our brand with a new website and logo. Our website is run through wordpress and hence we would need appropriate files and designs to accomodate this.
Our new logo should represent the idea of navigating a career path and exploring the unknown. Up until now it has been a compass in tones of purple and blue. We are happy to keep this motif but would need an updated, more representative logo. We are also happy to get some new ideas if the designer has something they think would fit.
The website itself should have fresh and clean look. We would like a banner at the top with clear links to the various parts of the site. The banner should stay consistent throughout the site.
We would like the main page to have a clean and simple look which places the focus on the profiles and their associated photos.
We would like pictographs to represent the different fields which our profiles fit into and would like to discuss with the winning designer what these would look like exactly. As a starting point we would like pictographs representing STEM (Science, Technology, Engineering, Mathematics) and SHAPE (Social Sciences, Humanities and Arts for People and the Economy).

We are really looking for something that is clean and professional but embodies our mission to represent all of the major industries which doctoral graduates can go on to work in. Those being, academia (universities), government, industry (private enterprise and companies), and third sector (Charities and think tanks etc.). Any design should cover all of these and not focus just on a big business or similar. It should also represent that we are not purely science focused, but all disciplines and are a broad church in that sense. We are open to various colour schemes and ideas but would like something that gives a professional but approachable feel, it should have elements of Oxford, but not suggest that we are only open to Calderwick University students or graduates.
Some sites that may be useful are:
https://kestrelguild.org/news-resources/projects/research-culture/ - talks about the different areas of employment we are trying to represent
https://www.famden-lv.ac.uk/ an oxford internal website that we like the presentation of.

Target Market(s)

Academic researchers with a PhD

Industry/Entity Type

Academic Careers

Colors
0054AA
0677BA
7BADD7
CADEEF
E8F1F8
00AB8E
00BBA5
67D7C9
C6EFE9
E9F9F6
FFF300
FFF600
FEFA6F
FFFEC7
FFFEE8
6B429C
8869AF
B7A5CE
E3DAEB
F3F0F8

Requirements
Must have
• A new logo
Should not have
• The existing logo

```html
<!DOCTYPE html>
<html lang="en">
<head>
<meta charset="utf-8">
<title>Brightmoor Hub – Explore Your Options Beyond Academia</title>
<link rel="stylesheet" href="https://fonts.googleapis.com/css2?family=Poppins:wght@400;500;600;700&display=swap">
<style>
:root{
  --purple:#6B429C;
  --purple-mid:#8869AF;
  --blue:#0054AA;
  --teal:#00AB8E;
  --ink:#222222;
  --muted:#6b6b6b;
  --mist:#ECEAF0;
  --footer:#121212;
  --white:#ffffff;
}
*{box-sizing:border-box;margin:0;padding:0}
html,body{width:1200px;height:2506px;overflow:hidden}
body{font-family:'Poppins',sans-serif;color:var(--ink);background:var(--white)}
.page{position:relative;width:1200px;height:2506px;overflow:hidden}
.abs{position:absolute}

/* header */
.site-header{left:0;top:0;width:1200px;height:78px;background:var(--white);box-shadow:0 2px 4px rgba(0,0,0,.12);z-index:2}
.brand{left:161px;top:16px;display:flex;align-items:center;gap:10px}
.brand-mark{width:34px;height:34px;background:var(--blue);border-radius:4px}
.brand-name{font-weight:600;font-size:20px;line-height:22px;color:var(--blue);text-transform:uppercase;letter-spacing:.3px}
.main-nav{left:465px;top:28px;display:flex;gap:20px;font-size:15px}
.main-nav a{color:var(--ink);text-decoration:none}
.main-nav a.current{color:var(--purple)}
.search-icon{left:1013px;top:28px}

/* hero */
.hero{left:0;top:80px;width:1200px;height:414px;background:linear-gradient(90deg,#6A3F9E 0%,#5a4aa8 45%,#1E58BB 100%);border-bottom:4px solid #d9d9e3}
.hero-photo{left:705px;top:22px;width:275px;height:392px;background:linear-gradient(180deg,#3e4a8f 0%,#1c3f5a 60%,#183848 100%);border-radius:120px 120px 0 0}
.hero-kicker{left:159px;top:160px;font-size:29px;font-weight:400;color:var(--white)}
.hero-title{left:159px;top:196px;font-size:39px;font-weight:700;color:var(--white)}
.hero-lede{left:161px;top:261px;width:380px;font-size:15.5px;line-height:23px;color:var(--white)}
.btn{display:flex;align-items:center;justify-content:center;font-weight:600;font-size:15px;border-radius:6px;height:57px;text-decoration:none}
.btn-light{border:2px solid var(--white);color:var(--white)}
.btn-teal{border:2px solid var(--teal);color:var(--teal);background:var(--white);box-shadow:0 3px 8px rgba(0,0,0,.08)}
.hero-btn{left:161px;top:337px;width:192px}

/* who we are */
.who-photo{left:161px;top:552px;width:323px;height:264px;border:5px solid var(--white);box-shadow:0 0 6px rgba(0,0,0,.2);background:linear-gradient(180deg,#7fb0e0 0%,#c9b98c 55%,#8a7a5a 100%)}
.section-title{font-size:28px;font-weight:600;color:var(--purple)}
.who-title{left:534px;top:594px}
.who-text{left:535px;top:644px;width:420px;font-size:15.5px;line-height:23px;color:var(--muted)}
.who-btn{left:535px;top:720px;width:188px}

/* get involved */
.involve{left:0;top:874px;width:1200px;height:438px;background:linear-gradient(90deg,#4b4a4c 0%,#5a5652 50%,#4c4e55 100%)}
.involve-title{left:159px;top:985px;font-size:30px;font-weight:600;color:var(--white)}
.involve-text{left:160px;top:1041px;width:360px;font-size:15.5px;line-height:23px;color:var(--white)}
.involve-btn{left:161px;top:1121px;width:170px}
.involve-photo{left:544px;top:932px;width:496px;height:321px;border:4px solid var(--white);background:linear-gradient(120deg,#c9d2da 0%,#9fb3c6 45%,#4f6f92 100%)}

/* recent profiles */
.profiles-title{left:0;top:1364px;width:1146px;text-align:center}
.profile{top:1429px;width:210px}
.profile-photo{width:201px;height:206px}
.profile-date{margin-top:18px;font-size:12px;color:var(--teal)}
.profile-name{margin-top:8px;font-size:19px;font-weight:500;line-height:20px;color:var(--ink)}
.profile-role{margin-top:4px;font-size:14px;font-weight:500;line-height:20px;color:var(--purple)}
.read-more{left:0;font-size:14px;font-weight:600;color:var(--teal);display:flex;align-items:center;gap:8px}
.carousel-btn{top:1629px;width:38px;height:38px;border-radius:50%;display:flex;align-items:center;justify-content:center}
.carousel-prev{left:107px;background:var(--white);box-shadow:0 2px 8px rgba(0,0,0,.15)}
.carousel-next{left:1055px;background:var(--purple-mid)}
.profiles-btn{left:504px;top:1843px;width:192px}

/* call to action */
.cta{left:0;top:1957px;width:1200px;height:245px;background:var(--mist)}
.cta-text{left:0;top:2012px;width:1200px;text-align:center;font-size:18.5px;font-weight:600;line-height:27px;color:var(--purple)}
.cta-btn{left:521px;top:2084px;width:158px}

/* footer */
.site-footer{left:0;top:2202px;width:1200px;height:304px;background:var(--footer);color:var(--white)}
.footer-brand{left:165px;top:2264px;display:flex;align-items:center;gap:10px}
.footer-brand .brand-name{color:var(--white);font-size:22px;line-height:24px}
.social{top:2348px;width:18px;height:18px;border-radius:50%;border:2px solid var(--white)}
.footer-heading{top:2258px;font-size:15px;font-weight:500}
.footer-list{list-style:none;font-size:12px;line-height:30px}
.contact-row{display:flex;align-items:center;gap:10px;font-size:12.5px}
.recent-list{list-style:none;font-size:12px;line-height:19.5px}
.recent-list .who{color:#8a8a8a}
.footer-rule{left:161px;top:2458px;width:878px;height:1px;background:#5a5a5a}
.copyright{left:0;top:2476px;width:1200px;text-align:center;font-size:10.5px;color:#9a9a9a}
</style>
</head>
<body>
<div class="page">

  <header class="site-header abs">
    <a class="brand abs" href="#" aria-label="Brightmoor Hub home">
      <span class="brand-mark"></span>
      <span class="brand-name">Brightmoor<br>Hub</span>
    </a>
    <nav class="main-nav abs">
      <a class="current" href="#">Home</a>
      <a href="#">Career Profiles</a>
      <a href="#">Get involved</a>
      <a href="#">Events</a>
      <a href="#">Resources</a>
      <a href="#">About us</a>
    </nav>
    <svg class="search-icon abs" width="24" height="24" viewBox="0 0 24 24" fill="none" stroke="#9a9a9a" stroke-width="2.4" stroke-linecap="round"><circle cx="10" cy="10" r="7.5"/><line x1="15.5" y1="15.5" x2="22" y2="22"/></svg>
  </header>

  <section class="hero abs">
    <div class="hero-photo abs" role="img" aria-label="Portrait of a professional woman in a dark blazer with arms crossed"></div>
  </section>
  <p class="hero-kicker abs">Explore Your Options</p>
  <h1 class="hero-title abs">Beyond Academia</h1>
  <p class="hero-lede abs">A collection of profiles of people who have made the transition from academia to industry.</p>
  <a class="btn btn-light hero-btn abs" href="#">Explore profiles</a>

  <div class="who-photo abs" role="img" aria-label="Aerial view of a domed university library under a blue sky"></div>
  <h2 class="section-title who-title abs">Who we are</h2>
  <p class="who-text abs">This website is edited by a group of DPhil students and researchers connected to Calderwick University.</p>
  <a class="btn btn-teal who-btn abs" href="#">Know About Us</a>

  <section class="involve abs" role="img" aria-label="Muted background view of historic university buildings"></section>
  <h2 class="involve-title abs">Get involved</h2>
  <p class="involve-text abs">See how you can contribute to the Brightmoor Hub: Options Beyond Academia project.</p>
  <a class="btn btn-light involve-btn abs" href="#">Find out how</a>
  <div class="involve-photo abs" role="img" aria-label="Colleagues in a meeting reviewing charts on a tablet"></div>

  <h2 class="section-title profiles-title abs" style="left:27px">Recent profiles</h2>

  <article class="profile abs" style="left:161px">
    <div class="profile-photo" role="img" aria-label="Portrait of Marisol Quintero-Vale" style="background:linear-gradient(180deg,#d8d4cf,#8d7a6a)"></div>
    <p class="profile-date">Apr 23, 2021</p>
    <h3 class="profile-name">Marisol<br>Quintero-Vale</h3>
    <p class="profile-role" style="width:160px">Behavioural Scientist at Fenwick Lab</p>
  </article>
  <article class="profile abs" style="left:386px">
    <div class="profile-photo" role="img" aria-label="Portrait of Tara Bhaskaran outdoors by water" style="background:linear-gradient(180deg,#4f6b3a,#2f5a86)"></div>
    <p class="profile-date">April 2, 2024</p>
    <h3 class="profile-name">Tara Bhaskaran</h3>
    <p class="profile-role" style="width:180px">Consultant at Independent/Freelance</p>
  </article>
  <article class="profile abs" style="left:611px">
    <div class="profile-photo" role="img" aria-label="Portrait of Elsa Harrow in a laboratory" style="background:linear-gradient(180deg,#e4e6e8,#d39aa4)"></div>
    <p class="profile-date">January 30, 2024</p>
    <h3 class="profile-name">Elsa Harrow</h3>
    <p class="profile-role" style="width:210px">Research Advisor at Lindale Women's Health Trust (LWHT)</p>
  </article>
  <article class="profile abs" style="left:837px">
    <div class="profile-photo" role="img" aria-label="Portrait of Nikos Arvanitis" style="background:linear-gradient(180deg,#e9e9e9,#4a5a6a)"></div>
    <p class="profile-date">February 1, 2024</p>
    <h3 class="profile-name">Nikos Arvanitis</h3>
    <p class="profile-role">Senior Scientist at Corvane Bio</p>
  </article>

  <a class="read-more abs" href="#" style="left:161px;top:1778px">Read More <svg width="18" height="10" viewBox="0 0 18 10" fill="none" stroke="#00AB8E" stroke-width="1.6"><line x1="0" y1="5" x2="16" y2="5"/><polyline points="12,1 16,5 12,9"/></svg></a>
  <a class="read-more abs" href="#" style="left:387px;top:1778px">Read More <svg width="18" height="10" viewBox="0 0 18 10" fill="none" stroke="#00AB8E" stroke-width="1.6"><line x1="0" y1="5" x2="16" y2="5"/><polyline points="12,1 16,5 12,9"/></svg></a>
  <a class="read-more abs" href="#" style="left:611px;top:1778px">Read More <svg width="18" height="10" viewBox="0 0 18 10" fill="none" stroke="#00AB8E" stroke-width="1.6"><line x1="0" y1="5" x2="16" y2="5"/><polyline points="12,1 16,5 12,9"/></svg></a>
  <a class="read-more abs" href="#" style="left:836px;top:1778px">Read More <svg width="18" height="10" viewBox="0 0 18 10" fill="none" stroke="#00AB8E" stroke-width="1.6"><line x1="0" y1="5" x2="16" y2="5"/><polyline points="12,1 16,5 12,9"/></svg></a>

  <button class="carousel-btn carousel-prev abs" style="border:0" aria-label="Previous profiles"><svg width="10" height="12" viewBox="0 0 10 12" fill="none" stroke="#333" stroke-width="1.6"><polyline points="7,1 2,6 7,11"/></svg></button>
  <button class="carousel-btn carousel-next abs" style="border:0" aria-label="Next profiles"><svg width="10" height="12" viewBox="0 0 10 12" fill="none" stroke="#ffffff" stroke-width="1.6"><polyline points="3,1 8,6 3,11"/></svg></button>

  <a class="btn btn-teal profiles-btn abs" href="#">Explore profiles</a>

  <section class="cta abs"></section>
  <p class="cta-text abs">If you’re a DPhil student or member of research staff at the University of Calderwick,<br>you can join the editorial team! Please contact us to find out more.</p>
  <a class="btn btn-teal cta-btn abs" href="#">Contact us</a>

  <footer class="site-footer abs"></footer>
  <div class="footer-brand abs">
    <span class="brand-mark" style="width:38px;height:38px"></span>
    <span class="brand-name">Brightmoor<br>Hub</span>
  </div>
  <span class="social abs" style="left:158px" aria-label="Social link"></span>
  <span class="social abs" style="left:204px" aria-label="Social link"></span>
  <span class="social abs" style="left:251px" aria-label="Social link"></span>
  <span class="social abs" style="left:296px" aria-label="Social link"></span>

  <h4 class="footer-heading abs" style="left:405px">Quick Links</h4>
  <ul class="footer-list abs" style="left:405px;top:2285px">
    <li>Home</li><li>About us</li><li>Accessibility</li>
  </ul>

  <h4 class="footer-heading abs" style="left:567px">Contact Us</h4>
  <div class="contact-row abs" style="left:567px;top:2291px">
    <svg width="18" height="18" viewBox="0 0 24 24" fill="none" stroke="#ffffff" stroke-width="1.5"><path d="M5 3h4l2 5-2.5 1.5a11 11 0 0 0 6 6L16 13l5 2v4a2 2 0 0 1-2 2A17 17 0 0 1 3 5a2 2 0 0 1 2-2z"/></svg>
    <span>(00) 123 456 789</span>
  </div>
  <div class="contact-row abs" style="left:567px;top:2325px">
    <svg width="20" height="16" viewBox="0 0 20 16" fill="none" stroke="#ffffff" stroke-width="1.4"><rect x="1" y="1" width="18" height="14" rx="1"/><polyline points="1,2 10,9 19,2"/></svg>
    <span>hello@brightmoor-hub.org</span>
  </div>

  <h4 class="footer-heading abs" style="left:798px">Recent Profiles</h4>
  <ul class="recent-list abs" style="left:798px;top:2291px">
    <li><span class="who">Marisol Quintero-Vale</span> June 12, 2024</li>
    <li><span class="who">Owen Fletcher</span> May 21, 2024</li>
    <li><span class="who">Tara Bhaskaran</span> April 2, 2024</li>
    <li><span class="who">Riya Sen</span> April 2, 2024</li>
    <li><span class="who">Emre Tolunay</span> March 28, 2024</li>
  </ul>

  <div class="footer-rule abs"></div>
  <p class="copyright abs">© 2024 Brightmoor Hub – All rights reserved</p>

</div>
</body>
</html>
```